Design a Chart Graphic that can be animated in video

We are looking for a clean and professional chart graphic that can be used on our website and edited to come alive in a video animation. The chart is to demonstrate that our product was proven to work in a clinical study. The chart title is Clinically Proven to Improve Sleep Quality. The x axis starts at "placebo" and ends at "tova calm" the placebo starts at 2% and the tova calm is 29% - the chart would show the rise from 2% to 29% in a dramatic way. The y axis would go from 0 - 30 %. There would be some sort of arrow to demonstrate the growth. Please see drawing for more clarity.

Target Market(s)

This is a study on SLEEP, the target market is sleep deprived men and women between the ages of 35-55.

Font styles to use
Sans Serif

Colors
0456a4
85abd2
85acd3
cedeed
ffffff
f04a50
fbed22

Requirements
Must have
• The chart must be delivered in a vector and styled in a way that can be animated by our video team. We are open to either flat or 3-D styles. The chart will be used on website and in video. It needs to look clean and professional, not funny or cartoonish. The color pallet needs to match www.itovacalm.com
• Please deliver vector, JPEG and PNG of the chart with and without a title.
Nice to have
• Fresh ideas to how to represent the chart in the most compelling way
Should not have
• Cartoons, gimmicky, colors other than those that match our website.

```html
<!DOCTYPE html>
<html lang="en">
<head>
<meta charset="UTF-8">
<title>Clinically Proven to Improve Sleep Quality</title>
<link rel="stylesheet" href="https://fonts.googleapis.com/css2?family=Montserrat:wght@400;500&display=swap">
<style>
  :root {
    --bg-light: #ffffff;
    --bg-shade: #e6e6e6;
    --grid: #ececec;
    --ring: #ffffff;
    --ink: #222222;
    --red: #f04a50;
    --red-bar: #c8363f;
    --orange: #ec8627;
    --yellow: #fbed22;
    --periwinkle: #6286ef;
    --sky: #29abe2;
    --sky-light: #5bc5ec;
    --ice: #9ad9f2;
    --navy: #0456a4;
  }
  * { margin: 0; padding: 0; box-sizing: border-box; }
  html, body { width: 1200px; height: 675px; overflow: hidden; }
  body {
    font-family: "Montserrat", sans-serif;
    background: linear-gradient(135deg, var(--bg-shade) 0%, #f6f6f6 40%, var(--bg-light) 75%);
    position: relative;
  }
  .chart { position: absolute; inset: 0; }

  .gridline {
    position: absolute;
    left: 347px;
    width: 567px;
    height: 4px;
    background: var(--grid);
    border-radius: 2px;
    box-shadow: 0 2px 3px rgba(0,0,0,0.08);
  }

  .tick {
    position: absolute;
    left: 288px;
    width: 56px;
    height: 56px;
    border-radius: 50%;
    background: var(--ring);
    box-shadow: 0 2px 6px rgba(0,0,0,0.14);
    display: flex;
    align-items: center;
    justify-content: center;
  }
  .tick span {
    width: 42px;
    height: 42px;
    border-radius: 50%;
    background: var(--c);
    box-shadow: 0 0 0 2px var(--ring), 0 0 0 3px var(--c);
    display: flex;
    align-items: center;
    justify-content: center;
    font-size: 11.5px;
    color: #ffffff;
  }
  .tick.dark-text span { color: var(--ink); }

  .bar {
    position: absolute;
    bottom: 143px;
    width: 54px;
    background: linear-gradient(to bottom, var(--c) 0%, var(--c) 78%, var(--d) 100%);
    box-shadow: 5px 2px 6px rgba(0,0,0,0.22);
  }

  .axis-label {
    position: absolute;
    top: 551px;
    font-size: 13px;
    font-weight: 500;
    color: var(--ink);
  }

  .growth-arrow { position: absolute; left: 0; top: 0; }
</style>
</head>
<body>
<div class="chart">
  <div class="gridline" style="top:136px"></div>
  <div class="gridline" style="top:203px"></div>
  <div class="gridline" style="top:269px"></div>
  <div class="gridline" style="top:335px"></div>
  <div class="gridline" style="top:402px"></div>
  <div class="gridline" style="top:469px"></div>
  <div class="gridline" style="top:534px"></div>

  <div class="tick" style="top:110px;--c:var(--navy)"><span>30%</span></div>
  <div class="tick" style="top:177px;--c:var(--sky)"><span>25%</span></div>
  <div class="tick" style="top:243px;--c:var(--sky-light)"><span>20%</span></div>
  <div class="tick" style="top:309px;--c:var(--periwinkle)"><span>15%</span></div>
  <div class="tick dark-text" style="top:376px;--c:var(--yellow)"><span>10%</span></div>
  <div class="tick dark-text" style="top:443px;--c:var(--orange)"><span>5%</span></div>
  <div class="tick dark-text" style="top:508px;--c:var(--red)"><span style="color:var(--ink)">0</span></div>

  <svg class="growth-arrow" width="1200" height="675" viewBox="0 0 1200 675" aria-hidden="true">
    <defs>
      <filter id="arrow-shadow" x="-10%" y="-10%" width="130%" height="130%">
        <feDropShadow dx="4" dy="3" stdDeviation="3" flood-color="#000" flood-opacity="0.18"/>
      </filter>
    </defs>
    <path fill="var(--yellow)" filter="url(#arrow-shadow)"
      d="M385,455 C500,428 585,340 652,224 L626,213 L713,156 L712,238 L688,226 C618,345 520,425 385,455 Z"/>
  </svg>

  <div class="bar" style="left:401px;height:18px;--c:var(--red-bar);--d:#a82a33"></div>
  <div class="bar" style="left:480px;height:60px;--c:var(--orange);--d:#a85a12"></div>
  <div class="bar" style="left:559px;height:113px;--c:var(--ice);--d:#5d8da3"></div>
  <div class="bar" style="left:638px;height:192px;--c:var(--periwinkle);--d:#3b4fa3"></div>
  <div class="bar" style="left:717px;height:267px;--c:var(--sky);--d:#1a6b8c"></div>
  <div class="bar" style="left:796px;height:377px;--c:var(--navy);--d:#023a70"></div>

  <div class="axis-label" style="left:403px">Placebo</div>
  <div class="axis-label" style="left:789px">Tova Calm</div>
</div>
</body>
</html>
```